TallonCryo Website - Biologics storage and handling

I would like a beginning design on a website for TallonCryo:

A Boston-based company dedicated to sourcing, storing, and supplying biologic materials of all kinds to the life sciences and scientific markets. From starting reagents, to basic and intermediate materials, to final synthesized and engineered products, we provide value throughout the biologics supply chain. TallonCryo provides backup, overflow, emergency, and stocking storage solutions to companies on a temporary or permanent basis. Life sciences companies can take advantage of the fact that the company is located in the middle of the Boston/Cambridge biotechnology corridor in order to have quick and efficient access to their cold chain materials. Out of state companies can leverage TallonCryo’s location for efficient distribution of materials to partner and client organizations. We also provide other value added services to organizations that do not have the local manpower, such as sourcing, supply, and distribution of materials.

The design should be mostly a white background with clean, linear, geometric colors added in according to the blue and orange color scheme represented in the corporate logo attached.

The website needs to communicate reliable service and provide the concept of a company dedicated to handling and providing client biological samples in a secure and efficient manner.

Some local competitors are:
1. Orlen BioServices: www.orlenbio-example.com
2. VaultiCore: www.vaulticore-example.com

From a design perspective, I like the Meridel Thera website:

www.merideltheraexample.com

Target Market(s)

Life sciences companies and other organizations

Industry/Entity Type

Biotechnology

Coding

Coded - Design and coding required

Number of Pages Required

5+ page

Font styles to use
Sans Serif

Colors
3176b5
0455a3
f37122

Requirements
Must have
• Tabs for pages:
About - Company information.
Platform - Inventory and sample management cloud platform; temperature profiling, logging, and reporting.
Services - Refrigeration and freezing services for biological samples, logistics services, sourcing services, courier services.
Updates - News, events, blog.
Login portal - Entry point for getting into platform. Maybe some freemium content here.
Nice to have
• Please be creative about website page sections, vibrant colors according to my established color scheme, and clean, linear, geometric shapes. I would like a white background with nice colors, clean lines and borders, and a very contemporary look. I want o
Should not have
• This is not a Business to Consumer business. This is a Business to Business enterprise. There should not be consumer oriented language. It is more about service and relationship management.

```html
<!DOCTYPE html>
<html lang="en">
<head>
<meta charset="utf-8">
<title>TallonCryo — Biologics Storage and Handling</title>
<link rel="stylesheet" href="https://fonts.googleapis.com/css2?family=Arimo:wght@400;700&display=swap">
<style>
:root{
  --blue:#3176b5;
  --navy:#0455a3;
  --orange:#f37122;
  --ink:#333;
  --muted:#777;
  --pale:#f8f8f9;
  --dark:#222224;
  --darker:#353537;
  --white:#fff;
}
*{margin:0;padding:0;box-sizing:border-box}
html,body{width:1200px;height:3883px;overflow:hidden;background:var(--white)}
body{position:relative;font-family:"Arimo",Arial,sans-serif;color:var(--ink)}
.abs{position:absolute}
a{text-decoration:none;color:inherit}

/* header */
.site-header{position:absolute;left:0;top:0;width:1200px;height:85px;background:var(--white)}
.brand{position:absolute;left:90px;top:36px;display:flex;align-items:center;gap:6px;font-size:16px;color:var(--navy)}
.brand-dot{width:10px;height:10px;background:var(--orange)}
.nav a{position:absolute;top:53px;font-size:14px;color:#222;letter-spacing:.2px}
.nav a.active{color:var(--blue)}
.login-btn{position:absolute;left:987px;top:33px;width:124px;height:38px;background:var(--orange);color:var(--white);font-size:14px;display:flex;align-items:center;justify-content:center}

/* hero */
.hero{position:absolute;left:0;top:85px;width:1200px;height:635px}
.hero-title{position:absolute;left:0;top:225px;width:1200px;text-align:center;color:var(--white);font-size:42px;line-height:51px;font-weight:400;text-shadow:0 1px 3px rgba(0,0,0,.25)}
.hero-rule{position:absolute;left:560px;top:354px;width:80px;height:3px;background:var(--orange)}
.dots{position:absolute;display:flex;gap:8px}
.dots span{width:7px;height:7px;border-radius:50%;border:1px solid var(--navy)}
.dots span.on{background:var(--navy)}

.section-title{position:absolute;left:0;width:1200px;text-align:center;font-size:31px;color:var(--navy);font-weight:400}
.section-title b{color:var(--orange)}

/* about */
.about-text{position:absolute;left:174px;top:840px;width:852px;text-align:center;font-size:12.6px;line-height:17px;color:#666}
.link-orange{position:absolute;color:var(--orange);font-size:13px;text-decoration:underline;text-align:center;width:200px}

/* services */
.service{position:absolute;top:1245px;width:200px}
.service svg{display:block;margin:0 auto}
.service-name{margin-top:30px;text-align:center;font-size:15px;line-height:19px;color:var(--navy)}
.service-name.hot{color:var(--orange)}
.view-btn{position:absolute;left:666px;top:1506px;width:62px;height:23px;background:var(--orange);color:var(--white);font-size:13px;display:flex;align-items:center;justify-content:center}

/* updates */
.tabs a{position:absolute;top:1928px;font-size:27px;color:#aaa}
.tabs a.active{color:var(--orange);border-bottom:2px solid var(--orange);padding-bottom:2px}
.card{position:absolute;top:2012px;width:235px}
.card-img{width:235px;height:190px}
.card h3{margin-top:33px;font-weight:400;font-size:17px;color:var(--navy)}
.card p{margin-top:8px;font-size:12.8px;line-height:16.4px;color:#888;text-align:justify}
.read-btn{display:inline-flex;align-items:center;justify-content:center;margin-top:14px;width:87px;height:31px;border:1px solid var(--orange);color:var(--orange);font-size:14px;letter-spacing:2.5px}
.read-btn.filled{background:var(--orange);color:var(--white)}

/* contact */
.contact-box{position:absolute;left:204px;top:2783px;width:780px;height:464px;background:var(--blue)}
.field{position:absolute;background:var(--white);font-size:14px;color:#aaa;padding:12px 10px}
.submit{position:absolute;left:537px;top:3158px;width:114px;height:33px;border-radius:17px;background:var(--orange);color:var(--white);font-size:15px;display:flex;align-items:center;justify-content:center}

/* footer */
.footer-brand{position:absolute;left:133px;top:3520px;display:flex;align-items:center;gap:10px;color:var(--white);font-size:28px;letter-spacing:.5px}
.footer-brand .mark{width:14px;height:14px;border:2px solid var(--white)}
.foot-col{position:absolute;top:3497px}
.foot-col h4{color:var(--orange);font-size:17px;font-weight:700;margin-bottom:18px}
.foot-col li{list-style:none;color:var(--white);font-size:15px;height:38px}
.foot-contact p{color:var(--white);font-size:15px;line-height:24px}
.socials{display:flex;gap:22px;margin-top:22px}
.socials span{width:17px;height:17px;border-radius:50%;border:2px solid var(--white)}
.bottom-bar{position:absolute;left:0;top:3817px;width:1200px;height:66px;background:var(--darker)}
.copyright{position:absolute;right:92px;top:23px;font-size:11px;color:#ccc}
</style>
</head>
<body>

<header class="site-header">
  <a class="brand" href="#"><span class="brand-dot"></span>TallonCryo</a>
  <nav class="nav">
    <a class="active" href="#" style="left:362px">HOME</a>
    <a href="#" style="left:446px">ABOUT</a>
    <a href="#" style="left:538px">PLATFORM</a>
    <a href="#" style="left:657px">SERVICES</a>
    <a href="#" style="left:770px">UPDATES</a>
  </nav>
  <a class="login-btn" href="#">Login / Sign Up</a>
</header>

<section class="hero">
  <svg class="abs" style="left:0;top:0" width="1200" height="635" role="img" aria-label="Scientist in blue gloves holding a test tube with a plant sprout in a laboratory">
    <defs>
      <linearGradient id="heroFill" x1="0" y1="0" x2="1" y2="1">
        <stop offset="0" stop-color="#9aa3ad"/>
        <stop offset=".35" stop-color="#dfe3e8"/>
        <stop offset=".6" stop-color="#c8d0da"/>
        <stop offset="1" stop-color="#8593a3"/>
      </linearGradient>
      <radialGradient id="heroGlove" cx=".5" cy=".55" r=".5">
        <stop offset="0" stop-color="#3b64c8" stop-opacity=".55"/>
        <stop offset="1" stop-color="#3b64c8" stop-opacity="0"/>
      </radialGradient>
    </defs>
    <polygon points="0,0 1200,0 1200,563 600,635 0,563" fill="url(#heroFill)"/>
    <polygon points="0,0 1200,0 1200,563 600,635 0,563" fill="url(#heroGlove)"/>
  </svg>
  <h1 class="hero-title">The Industrial Revolution of Drug<br>Discovery is Here</h1>
  <div class="hero-rule"></div>
  <div class="dots" style="left:581px;top:599px"><span class="on"></span><span></span><span></span></div>
</section>

<section class="about">
  <h2 class="section-title" style="top:763px">ABOUT <b>US</b></h2>
  <p class="about-text">TallonCryo is dedicated to sourcing, storing, and supplying biologic materials of all kinds to the life sciences and scientific markets. From starting reagents, to basic and intermediate materials, to final synthesized and engineered products, we provide value throughout the biologics supply chain. TallonCryo provides backup, overflow, emergency, and stocking storage solutions to companies on a temporary or permanent basis. Life sciences companies can take advantage of the fact that the company is located in the middle of the Boston/Cambridge biotechnology corridor in order to have quick and efficient access to their cold chain materials.</p>
  <a class="link-orange" href="#" style="left:500px;top:941px">Read More</a>
</section>

<section class="services">
  <svg class="abs" style="left:0;top:1019px" width="1200" height="715" aria-hidden="true">
    <polygon points="0,50 600,0 1200,50 1200,665 600,715 0,665" fill="var(--pale)"/>
  </svg>
  <h2 class="section-title" style="top:1117px">OUR <b>SERVICES</b></h2>

  <div class="service" style="left:208px">
    <svg width="166" height="188" viewBox="0 0 166 188">
      <polygon points="83,1 165,47 165,141 83,187 1,141 1,47" fill="none" stroke="var(--blue)" stroke-width="1.3"/>
      <g stroke="var(--navy)" stroke-width="3" fill="none">
        <line x1="50" y1="94" x2="86" y2="94"/><line x1="68" y1="76" x2="68" y2="112"/>
        <line x1="55" y1="81" x2="81" y2="107"/><line x1="81" y1="81" x2="55" y2="107"/>
        <path d="M96 66 v42 a9 9 0 1 0 10 0 v-42 a5 5 0 0 0 -10 0z"/>
        <line x1="112" y1="74" x2="120" y2="74"/><line x1="112" y1="84" x2="120" y2="84"/><line x1="112" y1="94" x2="120" y2="94"/>
      </g>
    </svg>
    <div class="service-name">Refrigeration and<br>Freezing Services</div>
  </div>

  <div class="service" style="left:402px">
    <svg width="166" height="188" viewBox="0 0 166 188">
      <polygon points="83,1 165,47 165,141 83,187 1,141 1,47" fill="none" stroke="var(--blue)" stroke-width="1.3"/>
      <g stroke="var(--navy)" stroke-width="3" fill="none">
        <rect x="46" y="76" width="46" height="34"/>
        <path d="M92 84 h14 l12 14 v12 h-26z"/>
        <circle cx="60" cy="113" r="6" fill="#fff"/><circle cx="104" cy="113" r="6" fill="#fff"/>
      </g>
    </svg>
    <div class="service-name">Logistics Services</div>
  </div>

  <div class="service" style="left:597px">
    <svg width="166" height="188" viewBox="0 0 166 188">
      <polygon points="83,1 165,47 165,141 83,187 1,141 1,47" fill="none" stroke="var(--blue)" stroke-width="1.3"/>
      <g stroke="#b8b8b8" stroke-width="3" fill="none">
        <path d="M58 88 a26 26 0 0 1 46 -10"/><polyline points="98,72 105,79 97,84"/>
        <path d="M108 100 a26 26 0 0 1 -46 10"/><polyline points="68,116 61,109 69,104"/>
      </g>
    </svg>
    <div class="service-name hot">Sourcing Services</div>
  </div>

  <div class="service" style="left:791px">
    <svg width="166" height="188" viewBox="0 0 166 188">
      <polygon points="83,1 165,47 165,141 83,187 1,141 1,47" fill="none" stroke="var(--blue)" stroke-width="1.3"/>
      <g stroke="var(--navy)" stroke-width="3" fill="none">
        <rect x="62" y="80" width="42" height="34"/>
        <line x1="62" y1="92" x2="104" y2="92"/><line x1="83" y1="80" x2="83" y2="92"/>
      </g>
    </svg>
    <div class="service-name">Courier Services</div>
  </div>

  <a class="view-btn" href="#">View</a>
  <a class="link-orange" href="#" style="left:500px;top:1605px">View All</a>
</section>

<section class="updates">
  <h2 class="section-title" style="top:1800px">LATEST <b>UPDATES</b></h2>
  <svg class="abs" style="left:216px;top:1913px" width="60" height="60" aria-hidden="true">
    <circle cx="30" cy="30" r="27" fill="none" stroke="#bbb" stroke-width="3"/>
    <polyline points="35,18 23,30 35,42" fill="none" stroke="#bbb" stroke-width="3"/>
  </svg>
  <svg class="abs" style="left:936px;top:1913px" width="60" height="60" aria-hidden="true">
    <circle cx="30" cy="30" r="27" fill="none" stroke="#bbb" stroke-width="3"/>
    <polyline points="25,18 37,30 25,42" fill="none" stroke="#bbb" stroke-width="3"/>
  </svg>
  <div class="tabs">
    <a href="#" style="left:426px">NEWS</a>
    <a class="active" href="#" style="left:556px">BLOG</a>
    <a href="#" style="left:667px">EVENTS</a>
  </div>

  <article class="card" style="left:217px">
    <div class="card-img" role="img" aria-label="Rows of glass lab bottles with blue liquid on a bench" style="background:linear-gradient(135deg,#e9f1f5,#a9d3e2 45%,#2d9bbd 75%,#e6eef2)"></div>
    <h3>Refrigeration and Freezing</h3>
    <p>Lorem ipsum, or lipsum as it is sometimes known, is dummy text used in laying out print, graphic or web designs. The passage is attributed to an unknown typesetter in the 15th</p>
    <a class="read-btn" href="#">Read</a>
  </article>
  <article class="card" style="left:488px">
    <div class="card-img" role="img" aria-label="Researcher examining a plant sample in a petri dish under blue light" style="background:linear-gradient(160deg,#6f96c9,#3a6db3 55%,#8fb0d8)"></div>
    <h3>Biological Samples</h3>
    <p>Lorem ipsum, or lipsum as it is sometimes known, is dummy text used in laying out print, graphic or web designs. The passage is attributed to an unknown typesetter in the 15th</p>
    <a class="read-btn filled" href="#">Read</a>
  </article>
  <article class="card" style="left:760px">
    <div class="card-img" role="img" aria-label="Gloved hands holding test tubes beside flasks of coloured liquid" style="background:linear-gradient(120deg,#eef0f3,#c9d2e6 40%,#6f8fd1 65%,#e8d9dd)"></div>
    <h3>Inventory and Sample</h3>
    <p>Lorem ipsum, or lipsum as it is sometimes known, is dummy text used in laying out print, graphic or web designs. The passage is attributed to an unknown typesetter in the 15th</p>
    <a class="read-btn" href="#">Read</a>
  </article>

  <div class="dots" style="left:581px;top:2462px"><span class="on"></span><span></span><span></span></div>
</section>

<section class="contact">
  <svg class="abs" style="left:0;top:2563px" width="1200" height="800" aria-hidden="true">
    <defs>
      <linearGradient id="contactFill" x1="0" y1="0" x2="0" y2="1">
        <stop offset="0" stop-color="#f6f7f9"/>
        <stop offset="1" stop-color="#eef0f3"/>
      </linearGradient>
    </defs>
    <polygon points="0,60 600,0 1200,60 1200,800 0,800" fill="url(#contactFill)"/>
  </svg>
  <h2 class="section-title" style="top:2676px">CONTACT <b>US</b></h2>
  <form class="contact-box">
    <div class="field" style="left:69px;top:74px;width:309px;height:42px">First Name*</div>
    <div class="field" style="left:401px;top:74px;width:309px;height:42px">Last Name*</div>
    <div class="field" style="left:69px;top:152px;width:309px;height:42px">email*</div>
    <div class="field" style="left:401px;top:152px;width:309px;height:42px">Phone*</div>
    <div class="field" style="left:69px;top:229px;width:641px;height:87px">Type your message......</div>
  </form>
  <a class="submit" href="#">SUBMIT</a>
</section>

<footer>
  <svg class="abs" style="left:0;top:3309px" width="1200" height="508" aria-hidden="true">
    <polygon points="0,0 600,72 1200,0 1200,508 0,508" fill="var(--dark)"/>
  </svg>
  <div class="footer-brand"><span class="mark"></span>TallonCryo</div>
  <div class="foot-col" style="left:482px">
    <h4>Menu</h4>
    <ul><li>Home</li><li>About</li><li>Platform</li><li>Services</li><li>Updates</li></ul>
  </div>
  <div class="foot-col" style="left:650px">
    <h4>Useful Link</h4>
    <ul><li>Terms &amp; Condition</li><li>Privacy Policy</li><li>About US</li><li>My Account</li></ul>
  </div>
  <div class="foot-col foot-contact" style="left:877px">
    <h4>Contact</h4>
    <p>Phone: +1 617 555 0148</p>
    <p>Email: hello@talloncryo-example.com</p>
    <div class="socials"><span></span><span></span><span></span><span></span></div>
  </div>
  <div class="bottom-bar"><p class="copyright">© 2020 talloncryo. All rights reserved.</p></div>
</footer>

</body>
</html>
```